KiteSurf Weather App Forecast Screen re-design (1 Screen)

We are redesigning our application, BreezeLoom. Our main screen is the forecast screen. The forecast screen presents the forecast for multiple places for the selected day.

Intro
-----

The user has a list of favorite spots that he is monitoring. Then he selects the date that he wants to get the forecast. The forecast screen presents a list of all the spots and a summary of the weather conditions. Spots are sorted by weather conditions. At the top, he gets the spot with the best weather conditions. We have an algorithm that can evaluate whether given weather conditions are good or not. When they are good we indicate that to the user.

Current Solution
------------------

There is also a landscape version, which contains a bit more data: "Current Forecast Screen Lanscape.jpeg". The landscape one is a bit funny, as it is taken from an Zentra Q and the app was not designed for it at the time.

The bars that you see for each hour use our algorithm to display whether the conditions are good:

- When the color is gray the conditions are not good
- When the color is yellow there are light wind conditions
- When the color is green there are good
- When the color is red the wind is very strong
- The height of the bar indicates wind strength

More Info
-----------

The detailed forecast screen is also attached so you can get a bit more context, "DetailedForecast.jpeg"

An example from an application that has a similar chart is attached, "SimilarApp.jpeg". I have circled the chart with red.

Future Solution
------------------

(See note.jpeg)

We want to create a page that contains more information and passes a better message to our users.

The elements that are important and we want to present to the user are the following:

1. Wind. (The most important)
It contains two elements: strength and direction.

1.1 Wind Strength.
Good wind strength is anything between 10-45 knots (measurement unit like km/h). The best representation with a color palette.
Gray will be the color used when the strength is not between 10-45.
The palette should start with yellow at 10 knots, then move toward green for 22knots and finally go towards red for 45 knots.

1.2 Wind Direction.
There are good wind directions that we can kite and directions that is is not possible.
Can be presented by an arrow that points in the direction the wind is blowing to. The color of the arrow will be green when the direction is good, yellow when it is average and gray when it is not good.

My thought for portrait mode is to use an arrow point for the direction and the color of the arrow to represent the strength. Solution number 2 on my notes. Then for landscape, we could use both a number and an arrow like number 4 on my notes.

2. Wave.
It contains three elements: height, period and direction. It is not displayed to all of our users only the ones that have selected the wave riding option.

2.1 Height is represented by a number. Ex. 1.2 meters or 2 foot.
2.2 Period is represented in seconds. Ex. 12 seconds.
2.3 Directions is an arrow that points to the direction the wave is coming from.

Again the solution should be like the wind. Arrow for direction and the color of the arrow for height. The palette here should be something with different blue colors.

3. Tide height. (Optional for tidal spots, as not all spots have tides)

The best way to represent that it through a graph. I would also like to see an alternative, where we have three symbols for low, mid and high tide.

4. General Weather. Rain/Snow and temperature.

This should be represented by a sun/cloud/rain symbol. If it is very cold the symbol can also contain an ice sign on the background.

---------

This is a guideline creativity will be valued. Maybe there is another way to do it that I have not thought about.

The winner of the competition will have to send us all graphics used in vector format, so we can input them to our xCode project.

Finally the person that wins the competition will be the first one to be considered for the redesign of the rest of our application.

Target Market(s)

Kitesurfers

Font styles to use
Sans Serif

Colors

Designer to choose colors to be used in the design.

Requirements
Must have
• It should be minimal and clearly communicate the weather forecast to my users. It should be user friendly.
Nice to have
• Communicative color palettes for both wind strength, tide and waves
Should not have
• Hard to understand UI

```html
<!DOCTYPE html>
<html lang="en">
<head>
<meta charset="utf-8">
<title>BreezeLoom – Wind Forecast</title>
<link href="https://fonts.googleapis.com/css2?family=Mulish:wght@300;400;600&display=swap" rel="stylesheet">
<style>
:root{
  --canvas:#d8f3f1;
  --screen:#f3f2fb;
  --bar:#ffffff;
  --ink:#222230;
  --green-a:#25b33e;
  --green-b:#4bd35e;
  --red-a:#f2384d;
  --red-b:#ee4a5d;
  --blue-a:#4b8fe6;
  --blue-b:#5c9cf0;
  --bar-grey:#bdbdbd;
  --bar-blue:#1a6ff0;
  --bar-red:#f24c63;
  --bar-green:#3cc94a;
  --arrow:#3a6ff0;
  --cloud:#3fa6d8;
}
*{margin:0;padding:0;box-sizing:border-box}
html,body{width:1200px;height:1082px;overflow:hidden}
body{background:var(--canvas);font-family:"Mulish",sans-serif;color:var(--ink);position:relative}
.screen{position:absolute;top:117px;width:463px;height:825px;background:var(--screen);border-radius:12px;overflow:hidden;box-shadow:0 4px 18px rgba(0,0,0,.08)}
.screen--list{left:85px}
.screen--detail{left:653px}
.status-bar{position:absolute;top:0;left:0;right:0;height:24px;font-size:14px;font-weight:600;background:var(--bar)}
.status-bar .time{position:absolute;left:0;right:0;text-align:center;top:3px}
.status-bar .signal{position:absolute;left:6px;top:5px}
.status-bar .battery{position:absolute;right:6px;top:3px;display:flex;align-items:center;gap:4px}
.app-header{position:absolute;top:24px;left:0;right:0;height:44px;background:var(--bar);box-shadow:0 2px 4px rgba(0,0,0,.06)}
.app-header h1{font-size:19px;font-weight:400;text-align:center;line-height:40px}
.app-header .menu{position:absolute;left:12px;top:12px}
.app-header .search{position:absolute;right:10px;top:9px}
.spot-card{position:absolute;left:12px;width:439px;height:236px;color:#fff;border-radius:2px;overflow:hidden;font-weight:300}
.spot-card--short{height:217px}
.spot-card .photo{position:absolute;inset:0}
.spot-card--good .photo{background:linear-gradient(180deg,var(--green-a),var(--green-b))}
.spot-card--strong .photo{background:linear-gradient(180deg,var(--red-a),var(--red-b))}
.spot-card--calm .photo{background:linear-gradient(180deg,var(--blue-a),var(--blue-b))}
.spot-card .date{position:absolute;top:24px;left:0;right:0;text-align:center;font-size:18px;opacity:.9}
.spot-card .wind-icon{position:absolute;left:120px;top:66px}
.spot-card .speed{position:absolute;left:194px;top:44px;font-size:72px;line-height:1;font-weight:300}
.spot-card .unit{position:absolute;left:284px;top:59px;font-size:19px;font-weight:400}
.spot-card .dir{position:absolute;left:284px;top:92px;font-size:19px;font-weight:400}
.spot-card .rating{position:absolute;top:122px;left:0;right:0;text-align:center;font-size:18px;opacity:.9}
.spot-card .city{position:absolute;left:10px;top:167px;font-size:26px}
.spot-card .weather-icon{position:absolute;left:171px;top:169px}
.spot-card .temp{position:absolute;left:214px;top:167px;font-size:26px;line-height:1.2}
.spot-card .deg{font-size:15px;vertical-align:10px}
.spot-card .wave-icon{position:absolute;left:291px;top:170px}
.spot-card .wave-height{position:absolute;left:325px;top:167px;font-size:26px;line-height:1.2}
.spot-card .dir-arrow{position:absolute;left:401px;top:171px}
.spot-card--no-dir .weather-icon{left:213px}
.spot-card--no-dir .temp{left:256px}
.spot-card--no-dir .wave-icon{left:333px}
.spot-card--no-dir .wave-height{left:367px}
.spot-card .hourly-link{position:absolute;top:208px;left:0;right:0;text-align:center;font-size:12px;font-weight:400;letter-spacing:.2px}
.spot-card .hourly-link svg{vertical-align:middle;margin-right:8px}
.hourly-panel{position:absolute;left:12px;top:298px;width:439px;height:250px;background:#f4f4fb}
.hourly-panel h2{position:absolute;left:12px;top:14px;font-size:14.5px;font-weight:400;color:#333}
.hourly-panel svg{position:absolute;left:0;top:0;overflow:visible}
.hourly-panel text{font-family:"Mulish",sans-serif}
</style>
</head>
<body>
<svg width="0" height="0" style="position:absolute">
  <defs>
    <symbol id="wind" viewBox="0 0 62 40"><g fill="none" stroke="#fff" stroke-width="3.5" stroke-linecap="round"><path d="M2 14h30a7 7 0 1 0-7-7"/><path d="M2 22h48a7 7 0 1 1-7 7"/><path d="M8 30h22"/><path d="M36 14h16a6 6 0 1 0-6-6"/></g></symbol>
    <symbol id="partly" viewBox="0 0 36 28"><g fill="none" stroke="#fff" stroke-width="2" stroke-linecap="round"><circle cx="22" cy="11" r="5"/><path d="M22 1v3M30 4l-2 2M33 11h-3M14 4l2 2"/><path d="M6 26h20a5 5 0 0 0 0-10 7 7 0 0 0-13-1 6 6 0 0 0-7 11z"/></g></symbol>
    <symbol id="wave" viewBox="0 0 30 26"><g fill="none" stroke="#fff" stroke-width="2" stroke-linejoin="round"><path d="M2 18c3-10 10-15 18-12 4 2 5 6 2 8-3-2-7 0-6 4H2z"/><path d="M2 22h26M2 25h26"/></g></symbol>
    <symbol id="nav" viewBox="0 0 24 24"><path d="M23 1 1 10l10 3 3 10z" fill="#fff"/></symbol>
    <symbol id="cloud" viewBox="0 0 24 16"><path d="M5 15h14a4.5 4.5 0 0 0 0-9 6 6 0 0 0-11-1A5 5 0 0 0 5 15z" fill="var(--cloud)"/></symbol>
    <symbol id="arrowsm" viewBox="0 0 16 16"><path d="M15 1 1 7l6 2 2 6z" fill="var(--arrow)"/></symbol>
  </defs>
</svg>

<section class="screen screen--list">
  <div class="status-bar">
    <svg class="signal" width="36" height="12" viewBox="0 0 36 12"><g fill="#000"><rect x="0" y="8" width="3" height="4"/><rect x="4" y="6" width="3" height="6"/><rect x="8" y="3" width="3" height="9"/><rect x="12" y="0" width="3" height="12"/></g><path d="M19 5a9 9 0 0 1 14 0M22 8a5 5 0 0 1 8 0" fill="none" stroke="#000" stroke-width="2"/><circle cx="26" cy="11" r="1.5"/></svg>
    <span class="time">9:41 AM</span>
    <span class="battery">✱ 100% <svg width="32" height="14" viewBox="0 0 32 14"><rect x="1" y="1" width="27" height="12" rx="3" fill="none" stroke="#000"/><rect x="3" y="3" width="23" height="8" rx="1.5"/><rect x="29" y="5" width="2" height="4"/></svg></span>
  </div>
  <header class="app-header">
    <svg class="menu" width="24" height="18" viewBox="0 0 24 18"><g stroke="#222" stroke-width="2"><path d="M0 2h24M0 9h24M0 16h24"/></g></svg>
    <h1>Wind Forecast</h1>
    <svg class="search" width="24" height="24" viewBox="0 0 24 24"><circle cx="10" cy="10" r="8" fill="none" stroke="#333" stroke-width="2"/><path d="M16 16l6 6" stroke="#333" stroke-width="2"/></svg>
  </header>

  <article class="spot-card spot-card--good" style="top:83px">
    <div class="photo" role="img" aria-label="Park view of Paris with the Eiffel Tower, tinted green"></div>
    <div class="date">Dec 25, 2017&nbsp;&nbsp;10:30am</div>
    <svg class="wind-icon" width="62" height="40"><use href="#wind"/></svg>
    <div class="speed">37</div><div class="unit">KTS</div><div class="dir">SW</div>
    <div class="rating">Normal Wind</div>
    <div class="city">Paris</div>
    <svg class="weather-icon" width="36" height="28"><use href="#partly"/></svg>
    <div class="temp">18<span class="deg">0</span>C</div>
    <svg class="wave-icon" width="30" height="26"><use href="#wave"/></svg>
    <div class="wave-height">1.3m</div>
    <svg class="dir-arrow" width="24" height="24"><use href="#nav"/></svg>
    <div class="hourly-link"><svg width="10" height="6" viewBox="0 0 10 6"><path d="M1 1l4 4 4-4" fill="none" stroke="#fff" stroke-width="1.4"/></svg>SEE HOURLY</div>
  </article>

  <article class="spot-card spot-card--strong" style="top:331px">
    <div class="photo" role="img" aria-label="London street with Big Ben clock tower, tinted red"></div>
    <div class="date">Dec 25, 2017&nbsp;&nbsp;10:30am</div>
    <svg class="wind-icon" width="62" height="40"><use href="#wind"/></svg>
    <div class="speed">73</div><div class="unit">KTS</div><div class="dir">SW</div>
    <div class="rating">Dangerous</div>
    <div class="city">London</div>
    <svg class="weather-icon" width="36" height="28"><use href="#partly"/></svg>
    <div class="temp">18<span class="deg">0</span>C</div>
    <svg class="wave-icon" width="30" height="26"><use href="#wave"/></svg>
    <div class="wave-height">1.3m</div>
    <svg class="dir-arrow" width="24" height="24"><use href="#nav"/></svg>
    <div class="hourly-link"><svg width="10" height="6" viewBox="0 0 10 6"><path d="M1 1l4 4 4-4" fill="none" stroke="#fff" stroke-width="1.4"/></svg>SEE HOURLY</div>
  </article>

  <article class="spot-card spot-card--calm spot-card--no-dir" style="top:579px">
    <div class="photo" role="img" aria-label="New Delhi city skyline, tinted blue"></div>
    <div class="date">Dec 25, 2017&nbsp;&nbsp;10:30am</div>
    <svg class="wind-icon" width="62" height="40"><use href="#wind"/></svg>
    <div class="speed">37</div><div class="unit">KTS</div><div class="dir">SW</div>
    <div class="rating">Calm Wind</div>
    <div class="city">New Delhi</div>
    <svg class="weather-icon" width="36" height="28"><use href="#partly"/></svg>
    <div class="temp">18<span class="deg">0</span>C</div>
    <svg class="wave-icon" width="30" height="26"><use href="#wave"/></svg>
    <div class="wave-height">1.3m</div>
    <div class="hourly-link"><svg width="10" height="6" viewBox="0 0 10 6"><path d="M1 1l4 4 4-4" fill="none" stroke="#fff" stroke-width="1.4"/></svg>SEE HOURLY</div>
  </article>
</section>

<section class="screen screen--detail">
  <div class="status-bar">
    <svg class="signal" width="36" height="12" viewBox="0 0 36 12"><g fill="#000"><rect x="0" y="8" width="3" height="4"/><rect x="4" y="6" width="3" height="6"/><rect x="8" y="3" width="3" height="9"/><rect x="12" y="0" width="3" height="12"/></g><path d="M19 5a9 9 0 0 1 14 0M22 8a5 5 0 0 1 8 0" fill="none" stroke="#000" stroke-width="2"/><circle cx="26" cy="11" r="1.5"/></svg>
    <span class="time">9:41 AM</span>
    <span class="battery">✱ 100% <svg width="32" height="14" viewBox="0 0 32 14"><rect x="1" y="1" width="27" height="12" rx="3" fill="none" stroke="#000"/><rect x="3" y="3" width="23" height="8" rx="1.5"/><rect x="29" y="5" width="2" height="4"/></svg></span>
  </div>
  <header class="app-header">
    <svg class="menu" width="24" height="18" viewBox="0 0 24 18"><g stroke="#222" stroke-width="2"><path d="M0 2h24M0 9h24M0 16h24"/></g></svg>
    <h1>Wind Forecast</h1>
    <svg class="search" width="24" height="24" viewBox="0 0 24 24"><circle cx="10" cy="10" r="8" fill="none" stroke="#333" stroke-width="2"/><path d="M16 16l6 6" stroke="#333" stroke-width="2"/></svg>
  </header>

  <article class="spot-card spot-card--good spot-card--short" style="top:81px">
    <div class="photo" role="img" aria-label="Park view of Paris with the Eiffel Tower, tinted green"></div>
    <div class="date">Dec 25, 2017&nbsp;&nbsp;10:30am</div>
    <svg class="wind-icon" width="62" height="40"><use href="#wind"/></svg>
    <div class="speed">37</div><div class="unit">KTS</div><div class="dir">SW</div>
    <div class="rating">Normal Wind</div>
    <div class="city">Paris</div>
    <svg class="weather-icon" width="36" height="28"><use href="#partly"/></svg>
    <div class="temp">18<span class="deg">0</span>C</div>
    <svg class="wave-icon" width="30" height="26"><use href="#wave"/></svg>
    <div class="wave-height">1.3m</div>
    <svg class="dir-arrow" width="24" height="24"><use href="#nav"/></svg>
  </article>

  <section class="hourly-panel">
    <h2>Hourly Wind Speed and Direction</h2>
    <svg width="439" height="250" viewBox="0 0 439 250">
      <g>
        <use href="#cloud" x="22" y="45" width="24" height="16"/>
        <use href="#cloud" x="70" y="45" width="24" height="16"/><circle cx="90" cy="46" r="3" fill="#f2c230"/>
        <use href="#cloud" x="119" y="45" width="24" height="16"/>
        <use href="#cloud" x="168" y="45" width="24" height="16"/>
        <use href="#cloud" x="216" y="45" width="24" height="16"/>
        <use href="#cloud" x="264" y="45" width="24" height="16"/>
        <use href="#cloud" x="313" y="45" width="24" height="16"/><path d="M327 59l-3 5h3l-2 4" stroke="#f2c230" stroke-width="1.5" fill="none"/>
        <use href="#cloud" x="362" y="45" width="24" height="16"/><path d="M376 59l-3 5h3l-2 4" stroke="#f2c230" stroke-width="1.5" fill="none"/>
        <circle cx="422" cy="52" r="5" fill="#f5b820"/><g stroke="#f5b820" stroke-width="1.5"><path d="M422 43v3M422 58v3M413 52h3M428 52h3M416 46l2 2M426 56l2 2M428 46l-2 2M416 58l2-2"/></g>
      </g>
      <g>
        <rect x="23" y="152" width="20" height="30" fill="var(--bar-grey)"/>
        <rect x="71" y="115" width="20" height="67" fill="var(--bar-blue)"/>
        <rect x="121" y="97" width="20" height="85" fill="var(--bar-red)"/>
        <rect x="170" y="165" width="20" height="17" fill="var(--bar-grey)"/>
        <rect x="218" y="128" width="20" height="54" fill="var(--bar-blue)"/>
        <rect x="266" y="96" width="20" height="86" fill="var(--bar-green)"/>
        <rect x="315" y="133" width="20" height="49" fill="var(--bar-red)"/>
        <rect x="364" y="114" width="20" height="68" fill="var(--bar-red)"/>
        <rect x="412" y="91" width="20" height="91" fill="var(--bar-green)"/>
      </g>
      <g font-size="12.5" fill="#333" text-anchor="middle">
        <text x="33" y="143">13</text><text x="81" y="105">19</text><text x="131" y="87">47</text>
        <text x="180" y="155">9</text><text x="228" y="118">19</text><text x="276" y="87">39</text>
        <text x="325" y="124">17</text><text x="374" y="106">30</text><text x="422" y="81">45</text>
      </g>
      <g>
        <use href="#arrowsm" x="25" y="198" width="16" height="16"/>
        <use href="#arrowsm" x="73" y="198" width="16" height="16"/>
        <use href="#arrowsm" x="123" y="198" width="16" height="16" transform="rotate(-60 131 206)"/>
        <use href="#arrowsm" x="172" y="198" width="16" height="16" transform="rotate(-120 180 206)"/>
        <use href="#arrowsm" x="220" y="198" width="16" height="16"/>
        <use href="#arrowsm" x="268" y="198" width="16" height="16" transform="rotate(-60 276 206)"/>
        <use href="#arrowsm" x="317" y="198" width="16" height="16" transform="rotate(-60 325 206)"/>
        <use href="#arrowsm" x="366" y="198" width="16" height="16"/>
        <use href="#arrowsm" x="414" y="198" width="16" height="16" transform="rotate(-60 422 206)"/>
      </g>
      <g font-size="12" fill="#888" text-anchor="middle">
        <text x="33" y="238">08 AM</text><text x="81" y="238">09 AM</text><text x="131" y="238">10 AM</text>
        <text x="180" y="238">11 AM</text><text x="228" y="238">12 AM</text><text x="276" y="238">01 PM</text>
        <text x="325" y="238">02 PM</text><text x="374" y="238">03 PM</text><text x="422" y="238">04 PM</text>
      </g>
    </svg>
  </section>

  <article class="spot-card spot-card--strong" style="top:560px;height:235px">
    <div class="photo" role="img" aria-label="London street with Big Ben clock tower, tinted red"></div>
    <div class="date">Dec 25, 2017&nbsp;&nbsp;10:30am</div>
    <svg class="wind-icon" width="62" height="40"><use href="#wind"/></svg>
    <div class="speed">73</div><div class="unit">KTS</div><div class="dir">SW</div>
    <div class="rating">Dangerous</div>
    <div class="city">London</div>
    <svg class="weather-icon" width="36" height="28"><use href="#partly"/></svg>
    <div class="temp">18<span class="deg">0</span>C</div>
    <svg class="wave-icon" width="30" height="26"><use href="#wave"/></svg>
    <div class="wave-height">1.3m</div>
    <svg class="dir-arrow" width="24" height="24"><use href="#nav"/></svg>
    <div class="hourly-link"><svg width="10" height="6" viewBox="0 0 10 6"><path d="M1 1l4 4 4-4" fill="none" stroke="#fff" stroke-width="1.4"/></svg>SEE HOURLY</div>
  </article>

  <article class="spot-card spot-card--calm" style="top:808px">
    <div class="photo" role="img" aria-label="City skyline, tinted blue"></div>
  </article>
</section>
</body>
</html>
```